Etiketten-Design für Qualitäts- und Prädikatswein
Zielgruppe
Qualitäts- und Prädikatsweine
Aufgabenstellung
Das Etikett muss auf der Weinflasche zweigeteilt sein.
Etikett vorne: Höhe 14,5 cm x Breite 6 cm:
Auf der Vorderseite sollen folgende Daten mit enthalten sein (Reihenfolge ist frei wählbar):
- Unser Logo (Datei: Logo)
- Name des Weins z.B. Velora
- Kategorie z.B. Beerenauslese
- Geschmackskategorie z.B. süß
- Jahrgang z.B. 2023
- Austria
Rückenetikett (Beispiel: Datei Rückenetikett): Höhe 11 cm x Breite 6 cm
Auf der Rückseite müssen folgende Daten vorhanden sein (Reihenfolge ist frei wählbar):
- Logo ganz oben
- Verkehrsbezeichnungen (Schriftgröße mind. 1,2 mm): Prädikatswein LN 4827163
- Herkunft (Schriftgröße mind. 1,2 mm): Wein aus Österreich Burgenland
- Nennvolumen (Schriftgröße mind. 6 mm): e 0,5 L
- Alkoholgehalt (Schriftgröße mind. 1,2 mm): Alc. 8,5 % Vol.
- Restzuckergehalt (Schriftgröße mind. 1,2 mm): süß
- Zutaten (Schriftgröße mind. 1,2 mm): Zutaten und ein QR-Code
- Platz für ein Zertifizierungslogo
- Allergenkennzeichnung (Schriftgröße mind. und max. 1,2 mm): Enthält Sulfite
- Abfüller (Schriftgröße mind. 1,2 mm):
Vertrieb:
Kalmor Nerisa GmbH
A-4638 Gols
www.kalmor-nerisa.com
Abfüller 5361842 A-4638 <---- (Schriftgröße mind. und max. 1,2 mm)
Kalmor Solenn ArtikelNr.: 3815/46
Da wir vor allem Prädikatsweine mit höchster Qualität herstellen, soll das Etikett dies auch wiederspiegeln. Den Hintergrund stellen wir uns schwarz vor. Der Hintergrund darf auch gerne eine grafische Musterrung beinhalten.
Alle Angaben müssen sich in den Dateien bearbeitbar sein, da sich diese Daten zum teil noch ändern werden. Die Dateien müssen wir Druckereien geeignet sein.
Update: Das Flaschenmaß ist Höhe 30 cm, Durchmesser unten 6 cm. Es handelt sich also um eine schlanke Flasche. Siehe Datei: Flasche

```html
<!DOCTYPE html>
<html lang="de">
<head>
<meta charset="utf-8">
<title>Velora Beerenauslese – Frontetikett</title>
<link rel="stylesheet" href="https://fonts.googleapis.com/css2?family=Cinzel:wght@400;500&family=Cormorant+Garamond:wght@500&family=Roboto:wght@400&display=swap">
<style>
  :root {
    --canvas: #ffffff;
    --gold: #d8c43c;
    --gold-deep: #b9a52a;
    --text-light: #f2f2f2;
    --text-soft: #b5b5b5;
    --rule: #8c8c8c;
    --vintage-red: #b3262b;
    --taste: #8e8e8e;
  }
  html, body {
    margin: 0;
    width: 1040px;
    height: 1200px;
    overflow: hidden;
    background: var(--canvas);
  }
  .front-label {
    position: absolute;
    left: 304px;
    top: 96px;
    width: 432px;
    height: 1008px;
  }
  .brand-name {
    font-family: "Cinzel", serif;
    font-size: 15px;
    fill: var(--text-light);
    letter-spacing: 0.5px;
  }
  .wine-name {
    font-family: "Cinzel", serif;
    font-size: 33px;
    fill: var(--text-light);
    letter-spacing: 1px;
  }
  .category {
    font-family: "Roboto", sans-serif;
    font-size: 10.5px;
    fill: var(--text-light);
    letter-spacing: 1.2px;
  }
  .vintage {
    font-family: "Cormorant Garamond", serif;
    font-size: 13px;
    fill: var(--vintage-red);
    letter-spacing: 6px;
  }
  .taste {
    font-family: "Cormorant Garamond", serif;
    font-size: 11px;
    fill: var(--taste);
    letter-spacing: 4px;
  }
  .origin {
    font-family: "Roboto", sans-serif;
    font-size: 7px;
    fill: var(--text-soft);
    letter-spacing: 6px;
  }
</style>
</head>
<body>
<svg class="front-label" viewBox="0 0 240 560" xmlns="http://www.w3.org/2000/svg">
  <defs>
    <linearGradient id="label-finish" x1="0" y1="0" x2="1" y2="0">
      <stop offset="0" stop-color="#3a3a3a"/>
      <stop offset="0.12" stop-color="#9a9a9a"/>
      <stop offset="0.22" stop-color="#2b2b2b"/>
      <stop offset="0.5" stop-color="#111111"/>
      <stop offset="0.8" stop-color="#1c1c1c"/>
      <stop offset="0.94" stop-color="#555555"/>
      <stop offset="1" stop-color="#2a2a2a"/>
    </linearGradient>
    <radialGradient id="motif-fade" cx="0.6" cy="0.45" r="0.6">
      <stop offset="0" stop-color="#3a3a3a" stop-opacity="0.7"/>
      <stop offset="1" stop-color="#1a1a1a" stop-opacity="0"/>
    </radialGradient>
  </defs>

  <path class="label-body"
        d="M10 37 H78 L120 105 L162 37 H230 Q240 37 240 47 V515 L120 545 L0 515 V47 Q0 37 10 37 Z"
        fill="url(#label-finish)"/>
  <path class="notch-edge" d="M78 37 L120 105 L162 37" fill="none" stroke="#ffffff" stroke-width="6"/>

  <path class="quality-tab" d="M88 0 H152 L120 66 Z" fill="var(--gold)"/>
  <rect x="106" y="8" width="28" height="36" rx="8" fill="var(--gold-deep)"
        role="img" aria-label="Traubenmotiv auf goldenem Reiter"/>

  <circle class="brand-mark" cx="120" cy="150" r="15" fill="none" stroke="var(--text-light)" stroke-width="1.2"/>
  <text class="brand-name" x="120" y="190" text-anchor="middle">Kalmor Solenn</text>

  <rect x="120" y="285" width="120" height="200" fill="url(#motif-fade)"
        role="img" aria-label="Weinblätter und Traube als dezentes Hintergrundmotiv"/>

  <line x1="40" y1="210" x2="200" y2="210" stroke="var(--rule)" stroke-width="0.8"/>
  <text class="wine-name" x="120" y="246" text-anchor="middle">VELORA</text>
  <line x1="40" y1="257" x2="200" y2="257" stroke="var(--rule)" stroke-width="0.8"/>
  <text class="category" x="120" y="284" text-anchor="middle">BEERENAUSLESE</text>

  <text class="vintage" x="123" y="339" text-anchor="middle">2023</text>
  <text class="taste" x="122" y="364" text-anchor="middle">süß</text>

  <rect x="70" y="430" width="90" height="40" rx="6" fill="#8f8f8f" opacity="0.45"
        role="img" aria-label="Zeichnung eines alten Rebstocks"/>

  <text class="origin" x="122" y="500" text-anchor="middle">AUSTRIA</text>
</svg>
</body>
</html>
```